Corporate Design für Garten- und Landschaftsbau
Sehr guter Desinger, sehr schnelle Reaktion auf Änderungswünsche, alles bestens gelaufen, jederzeit gerne wieder, vorbildlich.
Zielgruppe
-Garten- und Landschaftsbau
-Bagger- und Erdarbeiten
-Kellertrockenlegung
-Hausmeisterdienste
-Individuelle Gartengestaltung
Aufgabenstellung
Eventuell ein Baggerarm mit Baggerlöffel und oder einen Baum oder ein Strauch

```html
<!DOCTYPE html>
<html lang="de">
<head>
<meta charset="utf-8">
<title>Waltrup Garten- und Landschaftsbau – Geschäftsausstattung</title>
<link href="https://fonts.googleapis.com/css2?family=Lato:wght@400;700;900&display=swap" rel="stylesheet">
<style>
:root{
  --green-dark:#4a6f2c;
  --green-light:#93c01f;
  --ink:#222;
  --paper:#fff;
  --line:#555;
}
*{margin:0;padding:0;box-sizing:border-box}
html,body{width:785px;height:1200px;overflow:hidden;background:var(--paper);font-family:'Lato',sans-serif;color:var(--ink)}
.canvas{position:relative;width:785px;height:1200px}
.abs{position:absolute}

/* brand block */
.brand{position:absolute;text-align:center;transform:translateX(-50%)}
.brand-mark{display:block;margin:0 auto;border:3px solid var(--green-dark);border-radius:50%}
.brand-name{display:block;color:var(--green-dark);font-weight:900;line-height:1;letter-spacing:-.5px}
.brand-tag{display:block;color:var(--ink);white-space:nowrap}

.brand--main{left:392px;top:52px}
.brand--main .brand-mark{width:104px;height:104px;border-width:4px}
.brand--main .brand-name{font-size:62px;margin-top:8px}
.brand--main .brand-tag{font-size:13px;letter-spacing:3.6px;margin-top:2px}

/* letterhead */
.letter{left:157px;top:308px;width:468px;height:661px;border:1px solid var(--ink)}
.brand--letter{left:376px;top:19px}
.brand--letter .brand-mark{width:38px;height:38px;border-width:2px}
.brand--letter .brand-name{font-size:24px;margin-top:4px}
.brand--letter .brand-tag{font-size:8.5px;letter-spacing:2.3px;margin-top:2px}
.services{position:absolute;list-style:none}
.services li{position:relative;padding-left:8px;white-space:nowrap}
.services li::before{content:"";position:absolute;left:0;background:var(--green-dark)}
.services--letter{left:323px;top:108px;font-size:7.5px;line-height:12.6px}
.services--letter li::before{top:3.5px;width:4.5px;height:4.5px}
.sender{left:37px;top:135px;font-size:6px;color:#444}
.fold{left:0;top:247px;width:24px;border-top:1px solid #999}
.foot{top:602px;font-size:6px;line-height:8.5px;color:#333}
.foot--a{left:42px}.foot--b{left:163px}.foot--c{left:329px}

/* business cards */
.card{top:1033px;width:190px;height:123px;border:1px solid #bbb;background:var(--paper);overflow:hidden}
.card--front{left:203px}
.card--back{left:410px}
.brand--card{left:95px;top:12px}
.brand--card .brand-mark{width:27px;height:27px;border-width:2px}
.brand--card .brand-name{font-size:17px;margin-top:3px}
.brand--card .brand-tag{font-size:7px;letter-spacing:1.8px;margin-top:1px}
.card-band{left:0;top:72px;width:100%;height:51px;background:var(--green-dark)}
.services--card{top:8px;font-size:5px;line-height:8.6px;color:#fff}
.services--card li{padding-left:6px}
.services--card li::before{top:2.6px;width:3.2px;height:3.2px;background:#fff}
.services--card.col-a{left:10px}.services--card.col-b{left:99px}
.holder{left:17px;top:37px;font-size:8px;font-weight:700}
.contact{left:105px;font-size:5px;line-height:6px;display:flex;align-items:flex-start;gap:4px}
.contact svg{flex:none;width:10px;height:10px}
.contact span{padding-top:2px}
.web-rule{left:0;top:102px;width:100%;display:flex;align-items:center;gap:3px;font-size:5px}
.web-rule::before{content:"";flex:0 0 103px;border-top:1px solid var(--line)}
.web-rule::after{content:"";flex:1;border-top:1px solid var(--line)}
</style>
</head>
<body>
<div class="canvas">

  <div class="brand brand--main">
    <span class="brand-mark"></span>
    <span class="brand-name">WALTRUP</span>
    <span class="brand-tag">Garten- und Landschaftsbau</span>
  </div>

  <section class="abs letter">
    <div class="brand brand--letter">
      <span class="brand-mark"></span>
      <span class="brand-name">WALTRUP</span>
      <span class="brand-tag">Garten- und Landschaftsbau</span>
    </div>
    <ul class="services services--letter">
      <li>Garten- und Landschaftspflege</li>
      <li>Bagger und Erdarbeiten</li>
      <li>Kellertrockenlegung</li>
      <li>Hausmeisterdieste</li>
      <li>Individuelle Gartengestaltung</li>
      <li>Tersassen</li>
      <li>Pflasterarbeiten</li>
      <li>Wegbesfestigung</li>
    </ul>
    <p class="abs sender">GLW&nbsp; Lindenweg 4 55612 Tannenfeld</p>
    <div class="abs fold"></div>
    <p class="abs foot foot--a">GLW<br>Garten- und Landschaftsbau Waltrup<br>Lindenweg 4<br>55612 Tannenfeld</p>
    <p class="abs foot foot--b">Telefon: 0170 - 12 34 567<br>E-Mail: info@garten-landschaftsbau-waltrup.de</p>
    <p class="abs foot foot--c">Musterbank Mainz<br>IBAN: DE00 1234 5678 0000 1111 00<br>BIC: MUSTDEM1XXX</p>
  </section>

  <section class="abs card card--front">
    <div class="brand brand--card">
      <span class="brand-mark"></span>
      <span class="brand-name">WALTRUP</span>
      <span class="brand-tag">Garten- und Landschaftsbau</span>
    </div>
    <div class="abs card-band">
      <ul class="services services--card col-a">
        <li>Garten- und Landschaftspflege</li>
        <li>Bagger und Erdarbeiten</li>
        <li>Kellertrockenlegung</li>
        <li>Hausmeisterdieste</li>
      </ul>
      <ul class="services services--card col-b">
        <li>Individuelle Gartengestaltung</li>
        <li>Tersassen</li>
        <li>Pflasterarbeiten</li>
        <li>Wegbesfestigung</li>
      </ul>
    </div>
  </section>

  <section class="abs card card--back">
    <p class="abs holder">Max Muster</p>
    <div class="abs contact" style="top:36px">
      <svg viewBox="0 0 10 10"><circle cx="5" cy="5" r="4.5" fill="none" stroke="#222" stroke-width=".6"/><path d="M3.3 2.6l1 .9-.5.8c.4.8 1 1.4 1.8 1.8l.8-.5.9 1-.7.8C4.8 7.1 2.9 5.2 2.5 3.3z" fill="#222"/></svg>
      <span>0170 - 12 34 567</span>
    </div>
    <div class="abs contact" style="top:51px">
      <svg viewBox="0 0 10 10"><circle cx="5" cy="5" r="4.5" fill="none" stroke="#222" stroke-width=".6"/><text x="5" y="6.8" font-size="5.5" text-anchor="middle" font-family="Lato,sans-serif" fill="#222">@</text></svg>
      <span>info@galabau-waltrup.de</span>
    </div>
    <div class="abs contact" style="top:66px">
      <svg viewBox="0 0 10 10"><circle cx="5" cy="5" r="4.5" fill="none" stroke="#222" stroke-width=".6"/><path d="M5 2.2a1.8 1.8 0 0 1 1.8 1.8C6.8 5.4 5 7.6 5 7.6S3.2 5.4 3.2 4A1.8 1.8 0 0 1 5 2.2z" fill="#222"/><circle cx="5" cy="4" r=".6" fill="#fff"/></svg>
      <span>Lindenweg 4<br>55612 Tannenfeld</span>
    </div>
    <div class="abs web-rule"><span>www.galabau-waltrup.de</span></div>
  </section>

</div>
</body>
</html>
```